Property risk and finance brokerage company needs a business card design

Tarlow Financial requires a business card design. Please integrate existing logo (refer uploaded file).
hex codes used on logo #002649 #008ED6 #444F51 #ADAFAA
font used - Cinzel
Contact information
Renata Sollisford
Director
Mobile: 0491 738 205
email: r.sollisford@tarlowfinancial.example.au
website: www.tarlowfinancial.example.au
CRN : 918354
PO Box 527
Canterbury, Victoria, 3126
Horizontal orientation please
Finance

```html
<!DOCTYPE html>
<html lang="en">
<head>
<meta charset="utf-8">
<title>Tarlow Financial — Business Card</title>
<link rel="stylesheet" href="https://fonts.googleapis.com/css2?family=Cinzel:wght@400;700&display=swap">
<style>
  :root {
    --navy: #002649;
    --blue: #008ED6;
    --slate: #444F51;
    --silver: #ADAFAA;
    --card-dark: #3b3c3e;
    --backdrop: #e4e5e3;
  }
  html, body {
    margin: 0;
    padding: 0;
    width: 1200px;
    height: 873px;
    overflow: hidden;
    background: var(--backdrop);
  }
  .sheet {
    position: relative;
    width: 1200px;
    height: 873px;
    display: flex;
    align-items: center;
    justify-content: center;
    gap: 60px;
  }
  .card {
    width: 520px;
    height: 318px;
    display: block;
    box-shadow: 0 6px 18px rgba(0,0,0,0.18);
    font-family: "Cinzel", serif;
  }
  .name { fill: var(--blue); font-size: 22px; letter-spacing: 1.5px; }
  .role { fill: var(--silver); font-size: 11px; letter-spacing: 2px; }
  .phone { fill: var(--blue); font-size: 17px; letter-spacing: 1px; }
  .detail { fill: var(--silver); font-size: 6.8px; letter-spacing: 0.2px; }
  .crn { fill: var(--navy); font-size: 8px; letter-spacing: 1px; }
  .brand-main { fill: var(--silver); font-size: 34px; letter-spacing: 3px; }
  .brand-sub { fill: var(--silver); font-size: 15px; letter-spacing: 6px; }
</style>
</head>
<body>
<main class="sheet">

  <svg class="card card-contact" viewBox="0 0 520 318" aria-label="Contact side of business card">
    <rect width="520" height="318" fill="var(--card-dark)"/>

    <g class="name-band">
      <rect x="0" y="38" width="300" height="62" fill="var(--navy)"/>
      <line x1="20" y1="72" x2="300" y2="72" stroke="var(--blue)" stroke-width="0.8"/>
      <polygon points="300,38 344,69 300,100" fill="var(--blue)"/>
      <text class="name" x="22" y="63">RENATA SOLLISFORD</text>
      <text class="role" x="22" y="89">MANAGING DIRECTOR</text>
    </g>

    <g class="contact-block">
      <rect x="270" y="140" width="230" height="108" fill="var(--navy)"/>
      <text class="phone" x="282" y="164">0491 738 205</text>
      <text class="detail" x="282" y="182">r.sollisford@tarlowfinancial.example.au</text>
      <text class="detail" x="282" y="194">www.tarlowfinancial.example.au</text>
      <text class="detail" x="282" y="206">PO BOX 527</text>
      <text class="detail" x="282" y="218">CANTERBURY, VICTORIA, 3126</text>
      <g class="icons">
        <rect x="434" y="226" width="18" height="18" fill="var(--blue)"/>
        <rect x="454" y="226" width="18" height="18" fill="var(--blue)"/>
        <rect x="474" y="226" width="18" height="18" fill="var(--blue)"/>
        <rect x="439" y="230" width="8" height="11" rx="1.5" fill="var(--navy)"/>
        <polygon points="459,235 467,230 467,240" fill="var(--navy)"/>
        <rect x="477" y="230" width="12" height="8" fill="none" stroke="var(--navy)" stroke-width="1.4"/>
        <rect x="481" y="239" width="4" height="2" fill="var(--navy)"/>
      </g>
    </g>

    <g class="rule">
      <rect x="0" y="266" width="430" height="9" fill="var(--blue)"/>
      <rect x="14" y="250" width="130" height="13" fill="var(--blue)"/>
      <text class="crn" x="20" y="259.5">CREDIT REP NO. 918354</text>
      <g class="hatch" stroke="var(--blue)" stroke-width="3">
        <line x1="440" y1="276" x2="449" y2="265"/>
        <line x1="451" y1="276" x2="460" y2="265"/>
        <line x1="462" y1="276" x2="471" y2="265"/>
        <line x1="473" y1="276" x2="482" y2="265"/>
        <line x1="484" y1="276" x2="493" y2="265"/>
        <line x1="495" y1="276" x2="504" y2="265"/>
      </g>
    </g>
  </svg>

  <svg class="card card-brand" viewBox="0 0 520 318" aria-label="Brand side of business card">
    <defs>
      <pattern id="stripes" width="14" height="14" patternUnits="userSpaceOnUse" patternTransform="rotate(-22)">
        <rect width="14" height="6" fill="var(--blue)"/>
      </pattern>
    </defs>
    <rect width="520" height="318" fill="var(--navy)"/>
    <rect x="34" y="0" width="452" height="318" fill="url(#stripes)"/>

    <g class="brand-plate">
      <polygon points="110,56 410,56 432,78 432,240 410,262 110,262 88,240 88,78"
               fill="var(--card-dark)"/>
      <circle cx="260" cy="112" r="18" fill="var(--blue)"/>
      <text class="brand-main" x="260" y="180" text-anchor="middle">TARLOW</text>
      <text class="brand-sub" x="260" y="210" text-anchor="middle">FINANCIAL</text>
    </g>
  </svg>

</main>
</body>
</html>
```